Clinical psychologist - Psychotherapist business card

Hi everyone, I'm a clinical psychologist and psychotherapist, and I’m looking for a logo for my business card. The front will feature only the logo, while the back will include my contact details (and possibly a subtle touch of the logo). I've found two logos that I like, but the first one feels a bit childish—it lacks professionalism and doesn’t stand out from other similar designs. The second one, which I do like, unfortunately gives off a clinical, impersonal vibe.

Feel free to improvise—you don’t need to base the design on the logos I previously mentioned.

I generally prefer minimalistic designs that convey warmth, trust, and professionalism. I’d also like the card to have a bright background to make it feel inviting.

Additionally, I’m leaning toward using letterpress for the print technique, so the design should be compatible with that style—elegant, tactile, and clean. However, I’m still open to other options if they better suit the design.

UPDATE: I'm considering naming my business “Velmora” (top-level domain: .gr), so you could incorporate that as well.

Target Market(s)

Psychology clients, Psychiatrists, Social media users

Industry/Entity Type

Clinical psychologist - Psychotherapist

Contact Information for Business Card

To be added later on

Colors

Designer to choose colors to be used in the design.

Requirements
Nice to have
• Possibly my initials on the front side. They are Δ Κ (capital letters) or δ κ (small letters).
Should not have
• Portraits of famous psychologists

```html
<!DOCTYPE html>
<html lang="en">
<head>
<meta charset="utf-8">
<title>Velmora — Business Card</title>
<link rel="stylesheet" href="https://fonts.googleapis.com/css2?family=Arimo:wght@400;700&display=swap">
<style>
  :root {
    --backdrop: #e9e6e2;
    --card-white: #ffffff;
    --brand-blue: #29a8e0;
    --ink: #111418;
    --card-dark: #1c1c1d;
    --card-dark-edge: #262627;
    --icon-line: #2b3440;
  }
  * { box-sizing: border-box; margin: 0; padding: 0; }
  html, body {
    width: 1200px; height: 872px; overflow: hidden;
    background: var(--backdrop);
    font-family: "Arimo", Arial, sans-serif;
  }
  .canvas { position: relative; width: 1200px; height: 872px; }

  .card {
    position: absolute;
    width: 580px; height: 331px;
    border-radius: 26px;
    overflow: hidden;
    box-shadow: 0 10px 28px rgba(0,0,0,0.18);
  }

  /* Back side */
  .card--back {
    left: 500px; top: 80px;
    background: var(--card-dark);
    border: 1px solid var(--card-dark-edge);
  }
  .card--back .brand-name {
    position: absolute;
    left: 0; right: 0; top: 50%;
    transform: translateY(-50%);
    text-align: center;
    color: var(--brand-blue);
    font-weight: 700;
    font-size: 30px;
    letter-spacing: 0.32em;
    text-transform: uppercase;
  }

  /* Front side */
  .card--front {
    left: 120px; top: 460px;
    background: var(--card-white);
  }
  .card__curve { position: absolute; inset: 0; }

  .contact {
    position: absolute;
    left: 40px; top: 54px;
    color: var(--ink);
  }
  .contact__name {
    color: var(--brand-blue);
    font-weight: 700;
    font-size: 22px;
    line-height: 1;
    text-transform: uppercase;
  }
  .contact__role { font-size: 14px; margin-top: 4px; }
  .contact__address { font-size: 14px; line-height: 1.25; margin-top: 18px; }
  .contact__list { list-style: none; margin-top: 14px; font-size: 14px; }
  .contact__item { display: flex; align-items: center; gap: 10px; height: 20px; }
  .contact__item--plain { padding-left: 24px; }
  .contact__icon { width: 14px; height: 14px; flex: none; }

  .card--front .brand-name {
    position: absolute;
    left: 355px; width: 200px; top: 160px;
    text-align: center;
    color: var(--ink);
    font-weight: 700;
    font-size: 22px;
    letter-spacing: 0.34em;
    text-transform: uppercase;
  }
</style>
</head>
<body>
<main class="canvas">

  <section class="card card--back" aria-label="Card back">
    <p class="brand-name">Velmora</p>
  </section>

  <section class="card card--front" aria-label="Card front">
    <svg class="card__curve" viewBox="0 0 580 331" preserveAspectRatio="none" aria-hidden="true">
      <path d="M580 0 L580 331 L230 331 C 270 190, 360 70, 580 0 Z" fill="var(--brand-blue)"/>
    </svg>

    <div class="contact">
      <h1 class="contact__name">My Name</h1>
      <p class="contact__role">Founder &amp; Director</p>
      <p class="contact__address">P.O. Box, Street Name,<br>Countryname , ZIPCODE 0000</p>
      <ul class="contact__list">
        <li class="contact__item">
          <svg class="contact__icon" viewBox="0 0 14 14" aria-hidden="true">
            <circle cx="7" cy="7" r="6.3" fill="none" stroke="var(--icon-line)" stroke-width="1"/>
            <path d="M5 4 L6.2 5.4 L5.6 6.2 C6 7.2 6.8 8 7.8 8.4 L8.6 7.8 L10 9 L9.2 10 C6.8 9.8 4.2 7.2 4 4.8 Z" fill="var(--icon-line)"/>
          </svg>
          <span>210 555 0147</span>
        </li>
        <li class="contact__item">
          <svg class="contact__icon" viewBox="0 0 14 14" aria-hidden="true">
            <circle cx="7" cy="7" r="6.3" fill="none" stroke="var(--icon-line)" stroke-width="1"/>
            <rect x="5" y="3.5" width="4" height="7" rx="0.8" fill="none" stroke="var(--icon-line)" stroke-width="1"/>
          </svg>
          <span>694 555 0382</span>
        </li>
        <li class="contact__item">
          <svg class="contact__icon" viewBox="0 0 14 14" aria-hidden="true">
            <circle cx="7" cy="7" r="6.3" fill="none" stroke="var(--icon-line)" stroke-width="1"/>
            <rect x="3.8" y="4.8" width="6.4" height="4.4" fill="none" stroke="var(--icon-line)" stroke-width="1"/>
            <path d="M3.8 4.8 L7 7.4 L10.2 4.8" fill="none" stroke="var(--icon-line)" stroke-width="1"/>
          </svg>
          <span>hello@velmora.gr</span>
        </li>
        <li class="contact__item contact__item--plain">
          <span>www.velmora.gr</span>
        </li>
      </ul>
    </div>

    <p class="brand-name">Velmora</p>
  </section>

</main>
</body>
</html>
```